we need a new logo and business card and package label for my cake business.
looking for a fresh and standout design.

i have attached my old card to this.

Industry/Entity Type

Hospitality

Contact Information for Business Card

Rosalind Tremaine
email: rosit07@mailvex.net
facebook:www.faceplaza.net/rosiesweetovens
mobile:0438127906

Logo Text

Desserts By Rosie T

Font styles to use
Decorative

Colors
ed2930
f04a51
b768aa
0356a4
33a6d7

Requirements
Must have
• standout design
• grab attention

```html
<!DOCTYPE html>
<html lang="en">
<head>
<meta charset="utf-8">
<title>Desserts By Rosie T – Business Card</title>
<link rel="stylesheet" href="https://fonts.googleapis.com/css2?family=Alegreya:wght@400;500&display=swap">
<style>
  :root {
    --page: #ece9ee;
    --card: #ffffff;
    --lace: #e8dbef;
    --lace-deep: #dccaea;
    --plum: #8b3d9c;
    --plum-soft: #a56bb4;
    --mark: #9a5fb8;
  }
  * { margin: 0; padding: 0; box-sizing: border-box; }
  html, body { width: 1200px; height: 873px; overflow: hidden; }
  body {
    background: var(--page);
    font-family: "Alegreya", Georgia, serif;
    color: var(--plum);
    position: relative;
  }
  .card {
    position: absolute;
    top: 282px;
    width: 540px;
    height: 309px;
    background: var(--card);
    box-shadow: 0 6px 18px rgba(60, 40, 70, 0.18);
    overflow: hidden;
  }
  .card--front { left: 40px; }
  .card--back { left: 620px; }
  .lace-band {
    position: absolute;
    left: 0;
    width: 100%;
    height: 46px;
    background: linear-gradient(var(--lace), var(--lace-deep));
  }
  .lace-band--top { top: 0; }
  .lace-band--bottom { bottom: 0; background: linear-gradient(var(--lace-deep), var(--lace)); }

  .holder {
    position: absolute;
    left: 30px;
    top: 64px;
  }
  .holder__name {
    font-size: 27px;
    font-weight: 400;
    letter-spacing: 0.3px;
    line-height: 1.1;
  }
  .holder__title {
    font-size: 13px;
    color: var(--plum-soft);
    margin-top: 4px;
  }
  .contacts {
    position: absolute;
    left: 30px;
    top: 150px;
    list-style: none;
  }
  .contacts__item {
    display: flex;
    align-items: center;
    gap: 9px;
    font-size: 13px;
    font-weight: 500;
    height: 22px;
  }
  .contacts__icon {
    width: 15px;
    height: 15px;
    border-radius: 50%;
    background: var(--plum);
    display: flex;
    align-items: center;
    justify-content: center;
    flex: none;
  }
  .brand-name {
    font-family: "Alegreya", Georgia, serif;
    font-weight: 500;
    color: var(--mark);
    white-space: nowrap;
  }
  .card--front .brand-name {
    position: absolute;
    right: 28px;
    bottom: 64px;
    font-size: 17px;
  }
  .back-brand {
    position: absolute;
    left: 0;
    right: 0;
    top: 50%;
    transform: translateY(-50%);
    display: flex;
    align-items: center;
    justify-content: center;
    gap: 16px;
  }
  .back-brand__circle {
    width: 72px;
    height: 72px;
    border-radius: 50%;
    background: var(--mark);
    flex: none;
  }
  .card--back .brand-name { font-size: 30px; }
</style>
</head>
<body>
  <section class="card card--front">
    <div class="lace-band lace-band--top" role="img" aria-label="Lavender lace pattern border"></div>
    <div class="lace-band lace-band--bottom" role="img" aria-label="Lavender lace pattern border"></div>

    <div class="holder">
      <h1 class="holder__name">Rosalind Tremaine</h1>
      <p class="holder__title">Qualified Chef &amp; Pastry Chef</p>
    </div>

    <ul class="contacts">
      <li class="contacts__item">
        <span class="contacts__icon">
          <svg width="9" height="9" viewBox="0 0 24 24"><path fill="#fff" d="M6.6 10.8a15 15 0 0 0 6.6 6.6l2.2-2.2c.3-.3.7-.4 1-.2 1.1.4 2.3.6 3.6.6.6 0 1 .4 1 1V20c0 .6-.4 1-1 1A17 17 0 0 1 3 4c0-.6.4-1 1-1h3.5c.6 0 1 .4 1 1 0 1.3.2 2.5.6 3.6.1.3 0 .7-.2 1z"/></svg>
        </span>
        0438127906
      </li>
      <li class="contacts__item">
        <span class="contacts__icon">
          <svg width="9" height="9" viewBox="0 0 24 24"><path fill="#fff" d="M2 5h20v14H2z"/><path fill="none" stroke="#8b3d9c" stroke-width="2" d="M2 5l10 8 10-8"/></svg>
        </span>
        rosit07@mailvex.net
      </li>
      <li class="contacts__item">
        <span class="contacts__icon"></span>
        www.faceplaza.net/rosiesweetovens
      </li>
    </ul>

    <p class="brand-name">Desserts By Rosie T</p>
  </section>

  <section class="card card--back">
    <div class="lace-band lace-band--top" role="img" aria-label="Lavender lace pattern border"></div>
    <div class="lace-band lace-band--bottom" role="img" aria-label="Lavender lace pattern border"></div>

    <div class="back-brand">
      <span class="back-brand__circle"></span>
      <p class="brand-name">Desserts By Rosie T</p>
    </div>
  </section>
</body>
</html>
```